Private School social media templates / ads

We are a school in South Australia -around 40kms south of Adelaide. We have 2 campuses and need fresh looks for our social media advertising.

These ads need to be designed so that our team can use them and change headings as needed or images. Ideally, PSD files or InDesign files work best.

We would need you to use stock images initially so that we can then add student photos to the ads or, if you have a different suggestion we need to come up with fresh ideas to get our message across. Here is a bit of background:

A private Christian school - one campus in Morphett Vale in the south of Adelaide and our second campus in Aldinga - we are a smaller school compared to many larger ones, so our main focus of marketing is a messages along the lines of:
- Academic Excellence (see additional notes below on this topic)
- Respect and Values and Faith
- Student focused approach to teaching - smaller class sizes means no student is left behinid.

Parents give us feedback saying they like a school with good values and one that teaches respect but also is respectful. We have a strong no-bullying policy and our academics are excellent when comparing TREVOK data.

Note - Academic Excellence.
One thing I've tried to communicate is that academic excellence is not just about getting high marks, instead, it is about encouraging students to be the best they can be. So in the past headings like - Give your Child a Great Start - and similar have worked well. Also, a strong point is - At Kestrel Ridge, your child is never just a number, but a valued part of our community.

These are some starting points. One thing I'd like to encourage is creativity - almost every school uses the same old style of advertising - a pic of 1 or 2 students and a heading like - Principals Tours - book now.

We need to stand out from the crowd when we advertise our tours.

The main focus is to increase enrolment numbers. We have a good quality CRM running so all enquiries go through a Funnel System.

I've included logos and brand documents - however, we are happy to move away from the fonts and be a bit creative with colours and tones we use.

Also, I have included a series we called -Crayons and Comets - where we created tech/space-themed ads showing where students could be in the future. This campaign ran for 2 years now and we need a fresh look with this sort of impact.

Target Market(s)

Primarily female aged 25-49

Industry/Entity Type

education - private school adelaide

Font styles to use
Sans Serif
Other font styles liked:
• Roboto is currently used but open to suggestions. Do not use Mutal Feelings font.

Requirements
Must have
• brand and promote school and school principal tours
Nice to have
• In our brand guide, there are our colours, ideally using those colors and tones for design
Should not have
• no generic ad designs - what I mean is a picture of a smiling student with the heading - Principal's Tours now on

```html
<!DOCTYPE html>
<html lang="en">
<head>
<meta charset="utf-8">
<title>Kestrel Ridge Christian College – Happy Students Enjoy Learning</title>
<link rel="stylesheet" href="https://fonts.googleapis.com/css2?family=Montserrat:wght@800&family=Ubuntu:wght@400;500&display=swap">
<style>
  :root {
    --frame-blue: #12a0e2;
    --sky-white: #ffffff;
    --sky-pale: #d8eef9;
    --sky-mid: #7ecaef;
    --sky-deep: #14a2e2;
    --brand-blue: #3d8fd0;
    --ink: #111111;
    --paper: #ffffff;
    --social-violet: #a07ab0;
    --photo-dark: #2f2a29;
    --photo-umber: #4a3a30;
    --photo-sweater: #8a6c52;
    --photo-skin: #c79a7e;
    --photo-laptop: #b7b2aa;
  }
  * { margin: 0; padding: 0; box-sizing: border-box; }
  html, body { width: 800px; height: 1200px; overflow: hidden; background: var(--paper); }
  .ad {
    position: relative;
    width: 800px;
    height: 1200px;
    overflow: hidden;
    border: 11px solid var(--frame-blue);
    background: linear-gradient(180deg, var(--sky-white) 0%, var(--sky-white) 12%, var(--sky-pale) 40%, var(--sky-mid) 68%, var(--sky-deep) 100%);
    font-family: "Ubuntu", sans-serif;
  }
  .ad__photo {
    position: absolute;
    top: 0;
    right: 0;
    width: 480px;
    height: 100%;
    background:
      radial-gradient(ellipse 120px 170px at 330px 300px, var(--photo-skin) 0%, rgba(199,154,126,0.5) 50%, rgba(199,154,126,0) 100%),
      radial-gradient(ellipse 260px 220px at 120px 1050px, var(--photo-laptop) 0%, rgba(183,178,170,0) 100%),
      linear-gradient(180deg, var(--photo-dark) 0%, var(--photo-umber) 40%, var(--photo-sweater) 65%, var(--photo-sweater) 100%);
    -webkit-mask-image: linear-gradient(90deg, transparent 0%, rgba(0,0,0,0.6) 18%, #000 38%);
    mask-image: linear-gradient(90deg, transparent 0%, rgba(0,0,0,0.6) 18%, #000 38%);
  }
  .brand {
    position: absolute;
    top: 36px;
    left: 29px;
    display: flex;
    align-items: center;
    gap: 10px;
  }
  .brand__mark {
    width: 38px;
    height: 38px;
    border-radius: 50%;
    background: var(--brand-blue);
  }
  .brand__name {
    font-family: "Ubuntu", sans-serif;
    font-weight: 500;
    font-size: 18px;
    line-height: 19px;
    color: var(--brand-blue);
  }
  .headline {
    position: absolute;
    top: 206px;
    left: 36px;
    font-family: "Montserrat", sans-serif;
    font-weight: 800;
    font-size: 86px;
    line-height: 110px;
    letter-spacing: -1px;
    color: var(--paper);
    -webkit-text-stroke: 6px var(--ink);
    paint-order: stroke fill;
    text-transform: uppercase;
  }
  .headline span { display: block; }
  .message {
    position: absolute;
    top: 704px;
    left: 49px;
    width: 420px;
    font-family: "Ubuntu", sans-serif;
    font-weight: 500;
    font-size: 48px;
    line-height: 69px;
    color: var(--paper);
  }
  .message span { display: block; }
  .social {
    position: absolute;
    left: 42px;
    top: 1081px;
    width: 70px;
    height: 70px;
    border-radius: 50%;
    background: var(--social-violet);
  }
  .code {
    position: absolute;
    right: 10px;
    bottom: 18px;
    font-family: "Ubuntu", sans-serif;
    font-size: 14px;
    color: var(--ink);
  }
</style>
</head>
<body>
  <main class="ad">
    <div class="ad__photo" role="img" aria-label="Photo of a young adult student in a brown jumper focused on typing at a laptop"></div>

    <header class="brand">
      <span class="brand__mark" aria-hidden="true"></span>
      <span class="brand__name">Kestrel Ridge<br>Christian College</span>
    </header>

    <h1 class="headline">
      <span>Happy</span>
      <span>Students</span>
      <span>Enjoy</span>
      <span>Learning</span>
    </h1>

    <p class="message">
      <span>At Kestrel</span>
      <span>Ridge you child is</span>
      <span>valued,</span>
      <span>respected and</span>
      <span>cared for.</span>
    </p>

    <span class="social" role="img" aria-label="Social media link"></span>

    <span class="code">C 25</span>
  </main>
</body>
</html>
```